Webdesign  Seminare im Bereich persönliche Entwicklung, Spiritualität und Coaching
Webdesign Seminare im Bereich persönliche Entwicklung, Spiritualität und Coaching
Zielgruppe
Wir bieten Seminare im Bereich persönliche Entwicklung, Spiritualität und Coaching an. Unsere Zielgruppe umfasst Menschen zw. 18 und 75 jeglichen Berufsstandes, die sich dafür interessieren ihre tieferen innewohnenden Potenziale kennenzulernen und zu eröffnen.
Dieser Auftrag hier ist ein Teaser-Projekt. Wir wachsen konstant, möchten mehrere Folgeaufträge vergeben und suchen auf diesem Weg einen langfristigen Partner.
Aufgabenstellung
- keine esoterischen Klischee-Bilder, nichts Verspieltes
- unser Auftritt (hier vorerst die Website) soll wärmer wirken als dies aktuell der Fall ist, die Klarheit darf dabei jedoch nicht verloren gehen
- klar, warm, offen, vertraut, seriös
- das Logo darf verändert werden
Aktuell ist recht wenig Bildmaterial vorhanden. Hier wird demnächst nachproduziert. Bitte vorerst, wenn designtechnisch angebracht, Stockmaterial (als Platzhalter) verwenden.

```html
<!DOCTYPE html>
<html lang="de">
<head>
<meta charset="utf-8">
<title>WesensRaum – Julius Brandt</title>
<link href="https://fonts.googleapis.com/css2?family=Montserrat:wght@400;500;600;700&family=Lato:wght@400;700&display=swap" rel="stylesheet">
<style>
:root{
  --orange:#ee7a3a;
  --dark:#333333;
  --footer:#1e1e1e;
  --sand:#ecebe6;
  --card:#eeece7;
  --hero:#ebe9e4;
  --text:#555555;
  --head:#333333;
}
*{box-sizing:border-box;margin:0;padding:0}
html,body{width:1200px;height:4637px;overflow:hidden}
body{font-family:'Lato',sans-serif;color:var(--text);background:#fff;position:relative}
.abs{position:absolute}
section,header,footer{position:absolute;left:0;width:1200px}
.btn{position:absolute;background:var(--orange);color:#fff;font-family:'Lato',sans-serif;font-size:15px;display:flex;align-items:center;justify-content:center;gap:10px}
.btn svg{width:12px;height:12px}
.h2{position:absolute;left:0;width:1200px;text-align:center;font-family:'Montserrat',sans-serif;font-weight:400;color:var(--orange);font-size:25px;letter-spacing:2px;text-transform:uppercase}
.lead{position:absolute;left:250px;width:700px;text-align:center;font-size:12.5px;line-height:25px;color:#666}
.photo{position:absolute}

/* header */
.hero{top:0;height:450px;background:var(--hero)}
.logo{left:126px;top:24px;font-family:'Montserrat',sans-serif;font-size:22px;color:var(--dark);font-weight:500}
.logo small{display:block;font-size:12px;color:var(--orange);margin-left:128px;margin-top:-2px;font-weight:400}
.nav{left:540px;top:33px;display:flex;gap:33px;font-family:'Montserrat',sans-serif;font-size:12.5px;color:var(--dark)}
.welcome{left:126px;top:172px;font-family:'Montserrat',sans-serif;color:var(--orange);font-size:44px;letter-spacing:2px;font-weight:400}
.welcome-sub{left:128px;top:224px;font-family:'Montserrat',sans-serif;color:var(--dark);font-size:30px;letter-spacing:1px}
.name-tag{left:612px;top:122px;font-family:'Montserrat',sans-serif;color:var(--orange);font-size:22px}

/* band */
.band-line{height:4px;background:var(--orange)}
.band{top:453px;height:204px;background:var(--dark)}
.band-box{left:126px;top:0;width:318px;height:204px;background:var(--orange);color:#fff;font-size:12px;text-align:center;padding:50px 26px 0;line-height:17px}
.band-box p{margin-bottom:10px}
.band-item{top:50px;width:300px;text-align:center;color:#fff;font-family:'Montserrat',sans-serif;font-weight:700;font-size:13.5px;letter-spacing:1.5px}
.band-item svg.icon{display:block;margin:0 auto 22px;width:56px;height:56px}

/* about */
.about{top:666px;height:513px;background:#fff}
.about h2{position:absolute;left:144px;top:68px;font-family:'Montserrat',sans-serif;font-weight:500;font-size:30px;color:var(--orange);letter-spacing:2px}
.about .text{position:absolute;left:144px;top:114px;width:594px;font-size:13px;line-height:25px}
.about .text p{margin-bottom:25px}

/* videos */
.videos{top:1179px;height:561px;background:var(--sand)}
.vcard{position:absolute;top:195px;width:284px;height:207px;background:#fff;border-left:3px solid var(--orange)}
.vcard .photo{left:0;top:0;width:281px;height:164px}
.vcard .play{position:absolute;left:122px;top:62px;width:40px;height:40px;border-radius:50%;background:#fff;display:flex;align-items:center;justify-content:center}
.vcard .cap{position:absolute;left:0;top:176px;width:281px;text-align:center;font-size:13px;color:#555}
.arrow{position:absolute;width:18px;height:28px}

/* benefits */
.benefits{top:1740px;height:545px;background:#fff}
.benefits .h2 span{color:var(--dark)}
.bcard{position:absolute;top:136px;width:282px;height:330px;background:var(--card);border-left:4px solid var(--orange);padding:28px 22px 0 20px}
.bcard h3{font-family:'Montserrat',sans-serif;font-weight:600;font-size:17px;color:#444;letter-spacing:1px;line-height:25px;margin-left:6px;height:62px}
.bcard p{font-size:12.5px;line-height:25px;color:#666;margin-top:16px}

/* workshops */
.workshops{top:2285px;height:795px;background:var(--sand)}
.wcard{position:absolute;top:206px;width:284px;height:499px;background:#fff;border-left:3px solid var(--orange)}
.wcard .photo{left:0;top:0;width:281px;height:164px}
.wcard .stripe{position:absolute;right:22px;top:150px;width:84px;height:16px;background:var(--orange);transform:skewX(-30deg)}
.wcard h3{position:absolute;left:22px;top:185px;font-family:'Montserrat',sans-serif;font-weight:600;font-size:17px;color:#444;letter-spacing:1px}
.wcard p{position:absolute;left:22px;top:222px;width:240px;font-size:12.5px;line-height:25px;color:#666}
.wcard .btn{left:80px;top:413px;width:118px;height:50px}

/* application */
.apply{top:3080px;height:437px;background:#fff}
.apply h2{position:absolute;left:0;width:640px;text-align:center;top:202px;font-family:'Montserrat',sans-serif;font-weight:500;font-size:26px;color:var(--orange);letter-spacing:2px}
.apply .sub{position:absolute;left:0;width:640px;text-align:center;top:242px;font-size:13px;color:#555}
.apply .vline{position:absolute;left:539px;top:59px;width:2px;height:302px;background:var(--orange)}
.apply .text{position:absolute;left:585px;top:88px;width:475px;font-size:12.5px;line-height:25px;color:#666}

/* testimonial */
.voices{top:3517px;height:495px;background:var(--sand)}
.voices .quote{position:absolute;left:240px;top:56px;width:720px;text-align:center;font-size:15.5px;line-height:32px;color:#555}
.voices .who{position:absolute;left:0;width:1200px;top:256px;text-align:center;font-weight:700;font-size:17px;color:#444}
.dots{position:absolute;left:537px;top:305px;display:flex;gap:18px}
.dots i{width:15px;height:15px;border-radius:50%;background:#c9c8c4;display:block}
.dots i.on{background:#666}

/* newsletter */
.news{top:4012px;height:396px;background:linear-gradient(180deg,#a7c2d4 0%,#d4ccc4 35%,#e7b88f 62%,#f2b35b 80%,#c7895a 100%)}
.news .kicker{position:absolute;left:394px;top:56px;font-size:13px;color:#222}
.news h2{position:absolute;left:0;width:1200px;text-align:center;top:80px;font-family:'Montserrat',sans-serif;font-weight:400;font-size:25px;color:var(--orange);letter-spacing:2px}
.news label{position:absolute;left:428px;font-size:10px;color:#555}
.news .input{position:absolute;left:426px;width:346px;height:36px;background:#eeecea}

/* footer */
.foot{top:4408px;height:229px;background:var(--footer)}
.social{position:absolute;left:554px;top:48px;display:flex;gap:14px}
.social i{display:block;width:20px;height:20px;border-radius:50%;background:#fff}
.flinks{position:absolute;left:0;width:1200px;top:100px;display:flex;justify-content:center;gap:44px;color:#fff;font-size:13px}
.fline{position:absolute;left:97px;top:156px;width:1002px;height:1px;background:#777}
.copy{position:absolute;left:0;width:1200px;top:184px;text-align:center;color:#999;font-size:10px}
</style>
</head>
<body>

<header class="hero">
  <div class="abs logo">WesensRaum<small>Julius Brandt</small></div>
  <nav class="abs nav"><span>Start</span><span>Julius Brandt</span><span>WesensRaum</span><span>Termine</span><span>Blog</span><span>Kontakt</span></nav>
  <div class="abs welcome">Willkommen</div>
  <div class="abs welcome-sub">im WesensRaum</div>
  <div class="btn" style="left:126px;top:282px;width:119px;height:49px">Tritt ein! <svg viewBox="0 0 12 12"><path d="M1 6h9M6 2l4 4-4 4" stroke="#fff" stroke-width="2" fill="none"/></svg></div>
  <div class="abs name-tag">Julius Brandt</div>
  <svg class="abs" style="left:706px;top:168px" width="50" height="70" viewBox="0 0 50 70"><path d="M20 4C6 20 8 46 40 58" stroke="#333" stroke-width="2.5" fill="none"/><path d="M30 48l11 10-14 4" stroke="#333" stroke-width="2.5" fill="none"/></svg>
  <div class="photo" role="img" aria-label="Porträtfoto von Julius Brandt, lächelnd" style="left:770px;top:117px;width:275px;height:333px;background:radial-gradient(ellipse at 50% 45%,#e8c4aa 0%,#d9a98a 35%,#2a2a2a 70%,#ebe9e4 72%)"></div>
</header>
<div class="abs band-line" style="left:0;top:444px;width:1200px"></div>

<section class="band">
  <div class="abs band-box">
    <p>Du nimmst dein Leben bewusst wahr.</p>
    <p>Du lebst mit all deinen Sinnen und nutzt auch die „übernatürlichen".</p>
    <p>Du erkennst, dass alles mit dir verbunden ist.</p>
  </div>
  <div class="abs band-item" style="left:440px">
    <svg class="icon" viewBox="0 0 56 56"><path d="M28 48C10 34 4 26 4 17 4 9 10 4 17 4c5 0 9 3 11 7 2-4 6-7 11-7 7 0 13 5 13 13 0 9-6 17-24 31z" stroke="#ee7a3a" stroke-width="2.5" fill="none"/><path d="M10 26h10l4-8 5 14 4-6h13" stroke="#ee7a3a" stroke-width="2.5" fill="none"/></svg>
    LEBENDIG SEIN →
  </div>
  <div class="abs band-item" style="left:758px">
    <svg class="icon" viewBox="0 0 56 56" fill="none" stroke="#ee7a3a" stroke-width="2.5"><circle cx="18" cy="14" r="5"/><circle cx="38" cy="18" r="5"/><path d="M8 8l6 14v24M18 22v24M28 10l-6 12M46 12l-3 14v20M34 26v20"/></svg>
    FREI LEBEN →
  </div>
</section>
<div class="abs band-line" style="left:0;top:660px;width:1200px"></div>

<section class="about">
  <h2>JULIUS BRANDT</h2>
  <div class="text">
    <p>Es ist mir eine tiefe Herzensangelegenheit, die Menschen, welche in einem erweiterten Bewusstsein leben möchten, in das WesensRaum initial hineinzuführen, damit sie sich erinnern und all die Weisheit, Freiheit und Liebe wieder ganz bei sich wachrufen und integrieren können.</p>
    <p>Um dieser tiefgreifenden und lebensverändernden Arbeit gerecht zu werden, steht stetiges Lernen, Loslassen und Entwickeln für mich an erster Stelle. Ich begebe mich regelmäßig sowohl aktiv als auch unwillkürlich in tiefe Reinigungsprozesse und erlebe für mich, dass dieses eigene konsequente Vorangehen die unabdingbare Basis dafür ist, um andere Menschen erfolgreich begleiten zu können.</p>
  </div>
  <div class="btn" style="left:144px;top:388px;width:329px;height:49px">mehr über Julius Brandt erfahren <svg viewBox="0 0 12 12"><path d="M1 6h9M6 2l4 4-4 4" stroke="#fff" stroke-width="2" fill="none"/></svg></div>
  <div class="photo" role="img" aria-label="Julius Brandt im Gespräch vor einem Bücherregal" style="left:788px;top:127px;width:268px;height:285px;background:linear-gradient(135deg,#3b4a6b 0%,#6a6f7a 40%,#222 70%,#cfcfcf 100%)"></div>
  <div class="abs" style="left:756px;top:386px;width:200px;height:60px;background:var(--orange);transform:skewX(-28deg)"></div>
</section>

<section class="videos">
  <div class="h2" style="top:52px">Bewusstsein der neuen Zeit</div>
  <div class="lead" style="top:89px">Wir sind Julius und Johanna und sprechen auf diesem Kanal über Spiritualität, Selbstheilung, höhere Schwingungsebenen, Bewusstsein und eine bewusste Lebensgestaltung.</div>
  <svg class="arrow" style="left:88px;top:1467px;position:fixed" viewBox="0 0 18 28"></svg>
  <svg class="arrow" style="left:88px;top:287px" viewBox="0 0 18 28"><path d="M15 2L3 14l12 12" stroke="#ee7a3a" stroke-width="3" fill="none"/></svg>
  <svg class="arrow" style="left:1080px;top:287px" viewBox="0 0 18 28"><path d="M3 2l12 12L3 26" stroke="#ee7a3a" stroke-width="3" fill="none"/></svg>
  <div class="vcard" style="left:144px">
    <div class="photo" role="img" aria-label="Videostill: Gesprächsrunde im Studio" style="background:linear-gradient(160deg,#2c3b52,#6b7686 60%,#d8d8d8)"></div>
    <div class="play"><svg width="14" height="16" viewBox="0 0 14 16"><path d="M1 1l12 7-12 7z" fill="#111"/></svg></div>
    <div class="cap">Zeit im Umbruch.TV, 05.10.2021</div>
  </div>
  <div class="vcard" style="left:457px">
    <div class="photo" role="img" aria-label="Videostill: Interview im Studio" style="background:linear-gradient(160deg,#24405e,#5a7390 60%,#cfcfcf)"></div>
    <div class="play"><svg width="14" height="16" viewBox="0 0 14 16"><path d="M1 1l12 7-12 7z" fill="#111"/></svg></div>
    <div class="cap">Zeit im Umbruch.TV, 21.08.2020</div>
  </div>
  <div class="vcard" style="left:772px">
    <div class="photo" role="img" aria-label="Videostill: Julius Brandt vor Bücherregal" style="background:linear-gradient(135deg,#3b4a6b,#6a6f7a 45%,#2a2a2a 75%,#d0d0d0)"></div>
    <div class="play"><svg width="14" height="16" viewBox="0 0 14 16"><path d="M1 1l12 7-12 7z" fill="#111"/></svg></div>
    <div class="cap">NK TV, 05.06.2020</div>
  </div>
  <div class="btn" style="left:398px;top:451px;width:404px;height:50px"><span style="display:inline-block;width:26px;height:18px;border-radius:4px;background:#fff"></span> zum Videokanal von Julius Brandt <svg viewBox="0 0 12 12"><path d="M1 6h9M6 2l4 4-4 4" stroke="#fff" stroke-width="2" fill="none"/></svg></div>
</section>

<section class="benefits">
  <div class="h2" style="top:45px">Lesen im WesensRaum, <span>was bringt mir das?</span></div>
  <div class="bcard" style="left:128px"><h3>Schwingungserhöhung</h3><p>Deine körperliche und geistige Frequenz wird angehoben. Dies ermöglicht dir wieder wahrhaft fühlen zu können, eine erweiterte geistige Wahrnehmung und die Möglichkeit, deine eigenen höheren Energien und Potenziale zu öffnen und zu nutzen.</p></div>
  <div class="bcard" style="left:450px"><h3>Keine weitere Methode, die du lernst</h3><p>Es ist die Öffnung deines geistigen Sinns, der dir Informationen jenseits deiner 5 irdischen Sinne bietet. Dies ist dein Zugang zu unbegrenzten Möglichkeiten und wenn du so willst, zu einer unbegrenzten Anzahl von neuen Methoden.</p></div>
  <div class="bcard" style="left:774px"><h3>Inspiration und Kreativität</h3><p>Die Schwingung des WesensRaumes ist jenseits des menschlichen Verstandes – verbindet du dich damit, intensivierst du den Zugang zu deiner Intuition. Dies beschert dir ausgeprägtere Inspirationen und ermöglicht dir eine höhere Kreativität.</p></div>
</section>

<section class="workshops">
  <div class="h2" style="top:53px">Workshops</div>
  <div class="lead" style="top:97px">Schauen Sie sich diese Sammlung von Kursen und Meditationen an, die ich für Sie erstellt habe, damit Sie jetzt die Unterstützung erhalten, die Sie für echte Selbstfürsorge benötigen.</div>
  <svg class="arrow" style="left:88px;top:468px" viewBox="0 0 18 28"><path d="M15 2L3 14l12 12" stroke="#ee7a3a" stroke-width="3" fill="none"/></svg>
  <svg class="arrow" style="left:1080px;top:468px" viewBox="0 0 18 28"><path d="M3 2l12 12L3 26" stroke="#ee7a3a" stroke-width="3" fill="none"/></svg>
  <div class="wcard" style="left:144px">
    <div class="photo" role="img" aria-label="Gruppe jubelt mit erhobenen Armen auf einem Berg" style="background:linear-gradient(180deg,#dfe6ea,#c9b9a0 60%,#8a6d55)"></div>
    <div class="stripe"></div>
    <h3>BasisWorkshop</h3>
    <p>Im BasisWorkshop erlernst du den Zugang zum WesensRaum und wie du für dich und andere darin lesen und arbeiten kannst. Anhand unterschiedlicher Übungen erlangst du Sicherheit im Umgang mit dem Feld.</p>
    <div class="btn">Termine <svg viewBox="0 0 12 12"><path d="M1 6h9M6 2l4 4-4 4" stroke="#fff" stroke-width="2" fill="none"/></svg></div>
  </div>
  <div class="wcard" style="left:457px">
    <div class="photo" role="img" aria-label="Frau streckt die Hand in hellen Himmel über Wolken" style="background:linear-gradient(180deg,#e9eef1,#cfdde4 60%,#b9c9d2)"></div>
    <div class="stripe"></div>
    <h3>AufbauWorkshops</h3>
    <p>Um spezifische Themen und Entwicklungsbereiche noch intensiver und gezielter bearbeiten zu können, wurden die AufbauWorkshops entwickelt. Voraussetzung für die Teilnahme ist ein absolvierter BasisWorkshop.</p>
    <div class="btn">Termine <svg viewBox="0 0 12 12"><path d="M1 6h9M6 2l4 4-4 4" stroke="#fff" stroke-width="2" fill="none"/></svg></div>
  </div>
  <div class="wcard" style="left:772px">
    <div class="photo" role="img" aria-label="Zwei Menschen reichen sich am Berghang die Hand" style="background:linear-gradient(180deg,#e3ecef,#cdd8dc 55%,#6f7f5a)"></div>
    <div class="stripe"></div>
    <h3>Einzelsitzungen</h3>
    <p>Wenn du Themen oder Aufgaben in deinem Leben hast, bei denen du nicht weiterkommst, dann treten wir in das WesensRaum ein und rufen dort die notwendigen Informationen und Handlungshinweise für dich ab.</p>
    <div class="btn">Termine <svg viewBox="0 0 12 12"><path d="M1 6h9M6 2l4 4-4 4" stroke="#fff" stroke-width="2" fill="none"/></svg></div>
  </div>
</section>

<section class="apply">
  <svg class="abs" style="left:296px;top:98px" width="56" height="72" viewBox="0 0 56 72" fill="none" stroke="#333" stroke-width="2.5"><path d="M4 4h48v54l-10 10H4z"/><path d="M42 68V58h10"/><rect x="16" y="18" width="12" height="10"/><path d="M18 23l3 3 7-8"/><rect x="16" y="36" width="12" height="10"/><path d="M34 24h10M34 42h10"/></svg>
  <h2>ANWENDUNGSGEBIETE</h2>
  <div class="sub">Die Anwendungsgebiete sind nahezu unerschöpflich.</div>
  <div class="vline"></div>
  <div class="text">Die Anwendungsgebiete sind nahezu unerschöpflich. Da das WesensRaum mit allen Informationen verbunden ist, können Fragen aus vielfältigen Themengebieten beantwortet werden. Einschränkungen bestehen jedoch hinsichtlich konkreter Voraussagen für die Zukunft. Zum einen können unterschiedliche Entscheidungen die Zukunft verändern, zum anderen ist es nicht die Aufgabe des WesensRaumes dir wichtige Erfahrungen bereits im Vorfeld preiszugeben.</div>
  <div class="btn" style="left:585px;top:288px;width:174px;height:50px">mehr erfahren <svg viewBox="0 0 12 12"><path d="M1 6h9M6 2l4 4-4 4" stroke="#fff" stroke-width="2" fill="none"/></svg></div>
</section>

<section class="voices">
  <svg class="arrow" style="left:88px;top:137px" viewBox="0 0 18 28"><path d="M15 2L3 14l12 12" stroke="#ee7a3a" stroke-width="3" fill="none"/></svg>
  <svg class="arrow" style="left:1080px;top:137px" viewBox="0 0 18 28"><path d="M3 2l12 12L3 26" stroke="#ee7a3a" stroke-width="3" fill="none"/></svg>
  <div class="quote">Die Bereicherung, die dieser Kurs bietet, ist kaum in Worte zu fassen. Durch eine einfache und unkomplizierte Weise erfährt man, wie man intensiver mit seinem eigenen Selbst in Kontakt kommt. Für Fragen und Hilfestellungen stehen einem immer liebe Helfer zur Seite. Der Kurs ist wirklich für alle geeignet, selbst für die, die sich mit dem Thema „erweitertes Bewusstsein" noch nicht beschäftigt haben. Ich kann es nur jedem ans Herz legen, selber diese Erfahrung zu machen.</div>
  <div class="who">Karin Vogt, Bereichsleitung Marketing</div>
  <div class="dots"><i></i><i></i><i class="on"></i><i></i></div>
  <div class="btn" style="left:473px;top:360px;width:252px;height:50px">weitere Kundenstimmen <svg viewBox="0 0 12 12"><path d="M1 6h9M6 2l4 4-4 4" stroke="#fff" stroke-width="2" fill="none"/></svg></div>
</section>

<section class="news" role="img" aria-label="Hintergrund: Sonnenuntergang über Wolken">
  <div class="kicker">Stress abbauen müssen</div>
  <h2>FÜR NEWSLETTER ANMELDEN</h2>
  <label style="top:140px">E-Mail Adresse (erforderlich)</label>
  <div class="input" style="top:153px"></div>
  <label style="top:212px">name</label>
  <div class="input" style="top:226px"></div>
  <div class="btn" style="left:525px;top:298px;width:148px;height:49px">anmelden <svg viewBox="0 0 12 12"><path d="M1 6h9M6 2l4 4-4 4" stroke="#fff" stroke-width="2" fill="none"/></svg></div>
</section>

<footer class="foot">
  <div class="social"><i></i><i></i><i></i></div>
  <div class="flinks"><span>Impressum</span><span>Datenschutz</span><span>AGB</span><span>Kontakt</span></div>
  <div class="fline"></div>
  <div class="copy">© 2022 All Rights Reserved</div>
</footer>

</body>
</html>
```